WordPress Website Design & Theme - The Meridale Bidding House

Need a WordPress design for an auction company wanting a responsive, simple and easy to use site.

Please keep in mind that the design will be built on a responsive WP theme.

Colors will be light or white and complimentary/highlight colors from the logo.

Industry/Entity Type

It Company

Number of Pages Required

1 page

Font styles to use
Serif
Sans Serif

Requirements
Must have
• Navigation - 1) Home 2) Auction Calendar 3) Auction Results 4) For Sale 5) Services 6)About Us 7) Contact Us
• A site they mention liking is http://www.quenbrookbids.example/
• Site will have full width slideshow 960px. Use stock real estate photo. Header will have logo (attached) and contact info:
• THE MERIDALE BIDDING HOUSE
• P.O. Box 582
• Brackenford, TN 35817
• PHONE: (800)615-3087 or (318)382-9061
• FAX: (318)382-5148
• EMAIL: info@meridale-bidding.example
• There will be no sidebar on the homepage. There can be 3 horizontal widgets for "featured Listings", Join Our Newsletter, and maybe a form like http://www.meridale-bidding.example/request_proposal.php. The "Upcoming Auctions" feature as is seen on http://www.quenbrookbids.example/ will be used (attached image).
• In the footer: contact info, social media (FB, twitter, RSS), affiliation logos (attached), perhaps smaller company logo, News & Events blog, and if room "Featured Auctions".
Nice to have
• Use of drop-down menus styling- 1) Live Auctions 2) Online Auctions - under the Auction Calendar tab

```html
<!DOCTYPE html>
<html lang="en">
<head>
<meta charset="utf-8">
<title>The Meridale Bidding House</title>
<link href="https://fonts.googleapis.com/css2?family=Open+Sans:wght@400;600;700&display=swap" rel="stylesheet">
<style>
:root{
  --red:#d2243c;
  --red-dark:#b81d33;
  --navy:#3a2f63;
  --navy-deep:#2e2650;
  --text:#555;
  --muted:#8a8a8a;
  --line:#e3e3e3;
  --panel:#f4f5f7;
  --white:#fff;
}
*{box-sizing:border-box;margin:0;padding:0}
html,body{width:797px;height:1200px;overflow:hidden;background:var(--white)}
body{font-family:"Open Sans",Arial,sans-serif;color:var(--text);font-size:9px;position:relative}
.abs{position:absolute}
.top-bar{left:0;top:0;width:797px;height:8px;background:var(--red)}
.contact-item{display:flex;gap:10px;font-size:9.5px;line-height:14px;color:#444;white-space:nowrap}
.contact-item b{font-weight:600;color:#333}
.ring-icon{width:18px;height:18px;border:1px solid var(--red);border-radius:50%;flex:none;display:flex;align-items:center;justify-content:center}
.brand-mark{left:344px;top:6px;width:110px;height:110px;border-radius:50%;background:var(--white);border:3px solid var(--navy);display:flex;align-items:center;justify-content:center;text-align:center}
.brand-mark span{font-weight:700;color:var(--red);font-size:13px;line-height:15px}
.main-nav{left:99px;top:112px;width:599px;height:40px;background:var(--red);display:flex;align-items:center}
.main-nav a{color:var(--white);text-decoration:none;font-size:8.8px;font-weight:600;height:40px;display:flex;align-items:center;padding:0 15px}
.main-nav a.active{background:var(--navy);width:64px;justify-content:center;padding:0}
.hero{left:99px;top:156px;width:599px;height:292px;background:linear-gradient(180deg,#7fb2e0 0%,#b9d6ef 35%,#c9c2b4 55%,#7a9a55 78%,#5d8a3a 100%)}
.hero-title{left:99px;width:599px;text-align:center;color:var(--white);text-shadow:0 1px 3px rgba(0,0,0,.5)}
.dots{left:112px;top:425px;display:flex;gap:5px}
.dots i{width:9px;height:9px;border:1.5px solid var(--white);border-radius:50%;display:block}
.dots i.on{border-color:var(--red)}
.dropdown{left:163px;top:157px;width:120px;background:var(--red)}
.dropdown a{display:block;color:var(--white);font-size:9.5px;padding:0 0 0 22px;height:27px;line-height:27px;text-decoration:none;position:relative}
.dropdown a::before{content:"»";position:absolute;left:10px}
.widget-title{font-size:13px;font-weight:600;color:var(--navy);letter-spacing:.1px}
.widget-title em{font-style:normal;color:var(--red)}
.widget-text{font-size:8.5px;line-height:15.5px;color:#666}
.listing{list-style:none;font-size:8.7px;color:#666}
.listing li{display:flex;align-items:center;gap:11px;height:22px}
.listing li::before{content:"";width:7px;height:7px;border:1.5px solid var(--red);border-radius:50%;background:radial-gradient(var(--red) 35%,transparent 40%)}
.field{border:1px solid var(--line);background:var(--white);font-size:8.5px;color:#aaa;padding:0 8px;display:flex;align-items:center}
.btn-red{background:var(--red);color:var(--white);font-weight:700;font-size:10.5px;display:flex;align-items:center;justify-content:center;box-shadow:0 2px 0 var(--red-dark)}
.btn-navy{background:var(--navy);color:var(--white);font-size:9px;display:flex;align-items:center;justify-content:center}
.quote-box{left:503px;top:470px;width:195px;height:168px;border:1px solid var(--line);background:#f7f7f9}
.divider{left:99px;top:668px;width:599px;height:1px;background:var(--line)}
.card{background:var(--panel);text-align:center}
.card.raised{background:#f7f8fa;box-shadow:0 0 6px rgba(0,0,0,.18)}
.card p{font-size:8.6px;line-height:17.5px;color:#666;padding:0 14px}
.thumb{margin:0 auto;border:3px solid #8a6a3c}
.date-tag{background:#111;color:var(--white);font-size:7.5px;font-weight:700;display:inline-block;padding:2px 18px}
.view-more{color:var(--red);font-size:8.5px;text-decoration:underline}
.arrow-btn{width:25px;height:25px;border-radius:50%;border:1px solid #bbb;background:var(--white);display:flex;align-items:center;justify-content:center}
.footer{left:0;top:972px;width:797px;height:184px;background:var(--navy)}
.footer-mark{left:354px;top:928px;width:90px;height:90px;border-radius:50%;background:var(--white);border:3px solid var(--navy);display:flex;align-items:center;justify-content:center;text-align:center}
.footer-mark span{color:var(--red);font-weight:700;font-size:10.5px;line-height:12px}
.f-title{color:var(--white);font-size:10.5px;font-weight:600}
.f-row{display:flex;gap:9px;color:#d9d6e6;font-size:8px;line-height:11.5px;align-items:flex-start;white-space:nowrap}
.f-row svg{flex:none;margin-top:1px}
.f-row u{color:#e6e3f1}
.post{display:flex;gap:11px}
.post-date{width:31px;height:39px;border:1px solid #6d6494;color:#d9d6e6;font-size:8.5px;line-height:13px;display:flex;flex-direction:column;align-items:center;justify-content:center}
.post-text{font-size:8px;color:#d9d6e6;line-height:11px}
.post-text small{display:block;color:#9c96bb;font-size:8px;margin-top:5px}
.f-links{list-style:none}
.f-links li{color:#d9d6e6;font-size:8px;height:17.5px;display:flex;align-items:center;gap:9px}
.f-links li::before{content:"";border-left:4px solid #d9d6e6;border-top:3px solid transparent;border-bottom:3px solid transparent}
.badge{background:#e8e6ef;border-radius:4px}
.bottom-bar{left:0;top:1156px;width:797px;height:44px;background:var(--red)}
.copyright{left:100px;top:1174px;color:var(--white);font-size:8px}
.social{left:601px;top:1166px;display:flex;gap:7px}
.social i{width:27px;height:27px;border:1.5px solid var(--white);border-radius:50%;display:block}
</style>
</head>
<body>
<div class="abs top-bar"></div>

<header>
  <div class="abs" style="left:100px;top:30px;display:flex;flex-direction:column;gap:12px">
    <div class="contact-item"><span class="ring-icon"><svg width="9" height="9" viewBox="0 0 10 10"><path d="M2 1l2 2-1 1.2a6 6 0 0 0 2.8 2.8L7 6l2 2-1.3 1.3C4.5 9 1 5.5.7 2.3z" fill="none" stroke="#d2243c" stroke-width="1"/></svg></span><div><b>PHONE</b> &nbsp;: (800)615-3087 (or)<br>(318)382-9061</div></div>
    <div class="contact-item" style="align-items:center"><span class="ring-icon"><svg width="9" height="9" viewBox="0 0 10 10"><rect x="1.5" y="3.5" width="7" height="5" fill="none" stroke="#d2243c"/><rect x="3" y="1" width="4" height="2.5" fill="none" stroke="#d2243c"/></svg></span><div><b>FAX :</b> (318)382-5148</div></div>
  </div>
  <div class="abs brand-mark"><span>The Meridale<br>Bidding House</span></div>
  <div class="abs" style="left:514px;top:30px;display:flex;flex-direction:column;gap:12px">
    <div class="contact-item"><span class="ring-icon"><svg width="9" height="10" viewBox="0 0 10 12"><path d="M5 11S1.5 7 1.5 4.5a3.5 3.5 0 0 1 7 0C8.5 7 5 11 5 11z" fill="none" stroke="#d2243c"/><circle cx="5" cy="4.5" r="1.2" fill="#d2243c"/></svg></span><div><b>ADDRESS :</b> P.O. Box 582 Brackenford,<br>TN 35817</div></div>
    <div class="contact-item" style="align-items:center"><span class="ring-icon"><svg width="9" height="8" viewBox="0 0 10 8"><rect x=".5" y=".5" width="9" height="7" fill="none" stroke="#d2243c"/><path d="M.5 .5L5 4.5 9.5.5" fill="none" stroke="#d2243c"/></svg></span><div><b>EMAIL</b> &nbsp;: info@meridale-bidding.example</div></div>
  </div>
</header>

<nav class="abs main-nav">
  <a class="active">HOME</a><a>AUCTION CALENDAR</a><a>AUCTION RESULTS</a><a>FOR SALE</a><a>SERVICES</a><a>ABOUT US</a><a>CONTACT US</a>
</nav>

<section>
  <div class="abs hero" role="img" aria-label="Stock photo of a large suburban house with a green lawn and flowering shrubs under a blue sky"></div>
  <div class="abs hero-title" style="top:385px;font-size:12.5px">WELCOME TO</div>
  <div class="abs hero-title" style="top:401px;font-size:18px;font-weight:700">MERIDALE AUCTIONS</div>
  <div class="abs dots"><i></i><i></i><i class="on"></i><i></i><i></i></div>
  <div class="abs dropdown"><a>LIVE AUCTIONS</a><a>ONLINE AUCTIONS</a></div>
</section>

<section>
  <div class="abs" style="left:99px;top:472px;width:190px">
    <h2 class="widget-title">FEATURED <em>LISTINGS</em></h2>
    <p class="widget-text" style="margin-top:9px">The Meridale Bidding House, Inc. is a real estate auction company that specializes in with exciting auction events.</p>
    <ul class="listing" style="margin-top:8px">
      <li>Pinecrest Lake Golf Course</li>
      <li>Quiet Harbor Marina Auction</li>
      <li>Waterfront Home on Lake Verlow</li>
      <li>Ashgrove County Horse Farm</li>
    </ul>
  </div>
  <div class="abs" style="left:310px;top:472px;width:175px">
    <h2 class="widget-title">JOIN OUR <em>NEWSLETTER</em></h2>
    <p class="widget-text" style="margin-top:9px">The Meridale Bidding House, Inc. is a real estate auction company that specializes in combining cutting edge marketing exciting auction events.</p>
  </div>
  <div class="abs field" style="left:310px;top:570px;width:171px;height:30px">Enter your email id :</div>
  <div class="abs btn-red" style="left:309px;top:611px;width:70px;height:23px">SUBMIT</div>

  <div class="abs quote-box"></div>
  <h2 class="abs widget-title" style="left:514px;top:477px">REQUEST A <em>QUOTE</em></h2>
  <div class="abs field" style="left:516px;top:503px;width:85px;height:23px">First Name:</div>
  <div class="abs field" style="left:606px;top:503px;width:85px;height:23px">Last Name :</div>
  <div class="abs field" style="left:516px;top:530px;width:85px;height:23px">Phone :</div>
  <div class="abs field" style="left:606px;top:530px;width:85px;height:23px">Email :</div>
  <div class="abs field" style="left:516px;top:557px;width:175px;height:43px;align-items:flex-start;padding-top:7px">Property Description :</div>
  <div class="abs btn-navy" style="left:517px;top:608px;width:57px;height:23px">SUBMIT</div>
</section>

<div class="abs divider"></div>

<section>
  <div class="abs arrow-btn" style="left:68px;top:807px"><svg width="7" height="10" viewBox="0 0 7 10"><path d="M5.5 1L1.5 5l4 4" fill="none" stroke="#999" stroke-width="1.2"/></svg></div>
  <div class="abs arrow-btn" style="left:704px;top:807px"><svg width="7" height="10" viewBox="0 0 7 10"><path d="M1.5 1l4 4-4 4" fill="none" stroke="#999" stroke-width="1.2"/></svg></div>

  <div class="abs card" style="left:100px;top:728px;width:199px;height:182px;padding-top:29px">
    <div class="thumb" role="img" aria-label="Framed painting of a beach scene" style="width:53px;height:42px;background:linear-gradient(#9cc3dc,#e4d8b8)"></div>
    <span class="date-tag">March 31, 2016</span>
    <p style="margin-top:14px">It is a long established fact that a reader will be distracted by the readable content of a &nbsp;it look like readable English</p>
  </div>
  <div class="abs card raised" style="left:299px;top:696px;width:199px;height:214px;padding-top:28px">
    <div class="thumb" role="img" aria-label="Framed painting of a snowy village landscape" style="width:60px;height:47px;border-color:#3a2c1c;background:linear-gradient(#8aa2b8,#d8dde2 60%,#6b6a5a)"></div>
    <span class="date-tag">March 31, 2016</span>
    <p style="margin-top:14px">It is a long established fact that a reader will be distracted by the readable content of a &nbsp;it look like readable English</p>
    <div class="view-more" style="margin-top:8px">VIEW MORE INFO</div>
  </div>
  <div class="abs card" style="left:498px;top:728px;width:200px;height:182px;padding-top:30px">
    <div role="img" aria-label="Photo of a collection of antique dolls" style="width:64px;height:42px;margin:0 auto;background:linear-gradient(#cfcfcf,#8d7f7a)"></div>
    <span class="date-tag">April 6, 2016</span>
    <p style="margin-top:14px">It is a long established fact that a reader will be distracted by the readable content of a &nbsp;it look like readable English</p>
  </div>
</section>

<footer>
  <div class="abs footer"></div>
  <div class="abs footer-mark"><span>The Meridale<br>Bidding House</span></div>

  <h3 class="abs f-title" style="left:116px;top:1022px">CONTACT US</h3>
  <div class="abs" style="left:116px;top:1046px;display:flex;flex-direction:column;gap:10px;width:150px">
    <div class="f-row"><svg width="10" height="9" viewBox="0 0 10 9"><path d="M1 3c2-2 6-2 8 0v1H7V3H3v1H1z M2 5h6l1 3H1z" fill="#e6e3f1"/></svg>(800)615-3087 (Phone)</div>
    <div class="f-row"><svg width="10" height="9" viewBox="0 0 10 9"><rect x="1" y="3" width="8" height="5" fill="#e6e3f1"/><rect x="2.5" y="1" width="5" height="2" fill="#e6e3f1"/></svg>(318)382-5148 &nbsp;(Fax)</div>
    <div class="f-row"><svg width="10" height="8" viewBox="0 0 10 8"><rect x=".5" y=".5" width="9" height="7" fill="none" stroke="#e6e3f1"/><path d="M.5 .5L5 4.5 9.5.5" fill="none" stroke="#e6e3f1"/></svg><u>info@meridale-bidding.example</u></div>
    <div class="f-row"><svg width="10" height="10" viewBox="0 0 10 12"><path d="M5 11S1.5 7 1.5 4.5a3.5 3.5 0 0 1 7 0C8.5 7 5 11 5 11z" fill="#e6e3f1"/><circle cx="5" cy="4.5" r="1.3" fill="#3a2f63"/></svg>P.O. Box 582 Brackenford, TN<br>35817</div>
  </div>

  <h3 class="abs f-title" style="left:278px;top:1022px">NEWS &amp; EVENTS BLOG</h3>
  <div class="abs post" style="left:278px;top:1048px">
    <div class="post-date">25<span>FEB</span></div>
    <div class="post-text">The Meridale Bidding House, Inc.<br>is a real estate...<small>Read more</small></div>
  </div>
  <div class="abs post" style="left:278px;top:1100px">
    <div class="post-date">25<span>FEB</span></div>
    <div class="post-text">The Meridale Bidding House, Inc.<br>is a real estate...<small>Read more</small></div>
  </div>

  <h3 class="abs f-title" style="left:476px;top:1022px">FEATURED AUCTIONS</h3>
  <ul class="abs f-links" style="left:476px;top:1048px">
    <li>Live Auctions</li><li>Online Auctions</li><li>Auction Calendar</li><li>Auction Results</li>
  </ul>
  <div class="abs badge" style="left:590px;top:1064px;width:33px;height:40px"></div>
  <div class="abs badge" style="left:640px;top:1062px;width:44px;height:42px"></div>

  <div class="abs bottom-bar"></div>
  <div class="abs copyright">© COPY RIGHT2016 MERIDALE AUCTIONS . ALL RIGHTS RESERVED</div>
  <div class="abs social" aria-label="Social media links"><i></i><i></i><i></i></div>
</footer>
</body>
</html>
```